Website design for Keystone Bridge Advisory, a new boutique specialist consultancy company

We need a web design for a new company based in Australia called Keystone Bridge Advisory (this is abbreviated in our logo to KBA).

KBA is a boutique specialist advisory firm that provides Interim Management and Executive Transition Services. Through a suite of best practice methodologies coupled with advisory and consulting services, KBA supports businesses and executives during times of leadership hiatus and transition which not only mitigates risk of transition failure, but more importantly accelerates transition success.

Tobin at SketchHarbor has designed our logo (see attached file) and the logo and its colours will guide the website design. The primary colour scheme will be in the turquoise/aqua range and may include accent colours - designer's creative choice and guidance is welcome here.

The website should convey an image of crisp, modern professionalism. It's purpose will be to provide information about the company, our products and services and provide contact details. There is no online ordering or payment functionality required. Pages will include a home page with general information about the company, a number of content pages outlining information about each aspect of the services offered, an "about us" page and a "contact us" page.

Target Market(s)

This is a Busines-to-Business company and our target market is primarily large and medium sized companies. The specific individuals targeted at these companies will include:

Human Resources Directors
Talent and Recruitment Heads
Boards and Senior Executive teams of companies
Hiring managers responsible for recruiting and managing senior leaders and executives

Requirements
Should not have
• Online ordering / payment page

```html
<!DOCTYPE html>
<html lang="en">
<head>
<meta charset="utf-8">
<title>Keystone Bridge Advisory</title>
<link href="https://fonts.googleapis.com/css2?family=Ubuntu:wght@400;500&family=Roboto:wght@300;400&family=Oswald:wght@400&family=Montserrat:wght@500;600&display=swap" rel="stylesheet">
<style>
:root{
  --teal:#3dbcbd;
  --orange:#f05a28;
  --green:#8cc152;
  --green-light:#a3d468;
  --purple:#b594ea;
  --dark:#1d1d1d;
  --text:#555;
  --muted:#777;
  --line:#ddd;
}
*{box-sizing:border-box;margin:0;padding:0}
html,body{width:865px;height:1200px;overflow:hidden;background:#fff}
body{position:relative;font-family:"Ubuntu",sans-serif;color:var(--text)}
.abs{position:absolute}
.top-rule{left:0;top:0;width:865px;height:3px;background:var(--orange)}
.brand{left:72px;top:24px;display:flex;align-items:center;gap:8px}
.brand-dot{width:12px;height:12px;border-radius:50%;background:var(--orange)}
.brand-name{font-size:15px;font-weight:500;color:var(--teal);font-family:"Ubuntu",sans-serif}
.search{left:644px;top:32px;width:149px;height:28px;border:1px solid #ccc;font-size:9px;color:#666;padding:9px 11px;font-family:"Roboto",sans-serif}
.search svg{position:absolute;right:10px;top:7px}
.nav{left:72px;top:80px;width:721px;height:40px;background:var(--orange);display:flex;font-size:10px;color:#fff}
.nav span{display:flex;align-items:center;justify-content:center}
.nav .active{background:var(--teal)}
.hero{left:72px;top:128px;width:720px;height:318px;background:linear-gradient(100deg,#7d8fa6 0%,#a9bfd6 35%,#c9d7e6 55%,#5b74a0 80%,#40577f 100%)}
.hero-shadow{left:100px;top:446px;width:665px;height:14px;background:radial-gradient(ellipse at top,rgba(0,0,0,.22),transparent 70%)}
.hero-title{left:470px;top:264px;width:270px;text-align:center;font-family:"Oswald",sans-serif;font-size:21px;color:#fff;letter-spacing:-.3px;text-shadow:0 1px 2px rgba(0,0,0,.4)}
.arrow{width:24px;height:24px;border-radius:50%;background:#fff;border:2px solid #ccc;display:flex;align-items:center;justify-content:center}
.dots{left:417px;top:420px;display:flex;gap:4px}
.dots i{width:7px;height:7px;border-radius:50%;background:#fff;display:block}
.dots i.on{background:var(--orange)}
.welcome{left:72px;top:473px;width:721px;text-align:center;font-size:19px;color:var(--teal);font-weight:500}
.welcome b{color:var(--orange);font-weight:500}
.intro{left:76px;top:505px;width:713px;text-align:center;font-size:8.3px;line-height:17.5px;color:#444}
.section-title{font-size:19px;color:var(--orange)}
.services{left:72px;top:621px;width:721px;height:128px;display:flex}
.card{width:180px;height:128px;padding:14px 10px;color:#fff}
.card h3{font-size:13px;font-weight:500;margin-bottom:5px}
.card p{font-size:8px;line-height:13.6px}
.card.teal{background:var(--teal)}
.card.orange{background:var(--orange)}
.photo-meeting{width:180px;background:linear-gradient(135deg,#dfe5ea,#9aa7b3 60%,#3b4450)}
.photo-digital{width:180px;background:linear-gradient(135deg,#cfe7f3,#6fa7c9 50%,#2f5f86)}
.lower{left:64px;top:778px;width:734px;height:227px;background:#fafafa}
.heading-row{display:flex;align-items:center;gap:18px}
.heading-row span{font-size:15px;color:var(--orange)}
.heading-row i{flex:1;border-top:1px dashed #ccc}
.date{width:45px;height:45px;background:var(--teal);color:#fff;font-size:12px;line-height:15px;padding:7px 11px}
.pen{width:46px;height:45px;background:#fff;border:1px solid #ccc;border-radius:3px;display:flex;align-items:center;justify-content:center}
.post h4{font-size:12px;font-weight:400;color:#333;margin-bottom:5px}
.post p{font-family:"Roboto",sans-serif;font-weight:300;font-size:9.2px;line-height:15px;color:#666;width:225px}
.acc{width:351px;height:34px;border:1px solid #ccc;border-radius:3px;display:flex;background:#fff;font-family:"Roboto",sans-serif;font-size:9px;color:#666}
.acc .sign{width:34px;border-right:1px solid #ccc;display:flex;align-items:center;justify-content:center;font-size:16px;color:#888;font-weight:300}
.acc .label{display:flex;align-items:center;padding-left:10px}
.acc.open{background:var(--teal);border-color:var(--teal);color:#fff;font-family:"Ubuntu",sans-serif;font-size:10px;height:32px}
.acc.open .sign{border-color:rgba(255,255,255,.5);color:#fff}
.acc-body{font-family:"Roboto",sans-serif;font-weight:300;font-size:9.2px;line-height:15px;color:#666;width:340px}
.newsletter{left:0;top:1020px;width:865px;height:88px;background:var(--green);overflow:hidden}
.newsletter svg{position:absolute;left:0;top:0}
.nl-title{left:70px;top:10px;font-family:"Montserrat",sans-serif;font-weight:600;font-size:17.5px;color:#fff}
.nl-text{left:70px;top:39px;width:350px;font-family:"Montserrat",sans-serif;font-weight:500;font-size:8px;line-height:11px;color:#fff}
.nl-input{left:538px;top:30px;width:170px;height:28px;background:#f1f1f1}
.nl-btn{left:708px;top:30px;width:83px;height:28px;background:var(--purple);color:#fff;font-family:"Montserrat",sans-serif;font-weight:600;font-size:8.5px;display:flex;align-items:center;justify-content:center}
.footer-rule{left:0;top:1108px;width:865px;height:4px;background:var(--orange)}
.footer{left:0;top:1112px;width:865px;height:88px;background:var(--dark);color:#eee;font-family:"Roboto",sans-serif;font-size:8.8px}
.footer .links{position:absolute;left:71px;top:24px}
.footer .copy{position:absolute;left:71px;top:42px}
.social{position:absolute;top:24px;display:flex;gap:7px;left:700px}
.social i{width:26px;height:26px;border-radius:50%;background:#e9e9e9;display:block}
</style>
</head>
<body>
<div class="abs top-rule"></div>

<div class="abs brand"><span class="brand-dot"></span><span class="brand-name">Keystone Bridge Advisory</span></div>

<div class="abs search">Search
  <svg width="14" height="14" viewBox="0 0 14 14"><circle cx="6" cy="6" r="4.5" fill="none" stroke="#111" stroke-width="1.8"/><line x1="9.3" y1="9.3" x2="13" y2="13" stroke="#111" stroke-width="2"/></svg>
</div>

<nav class="abs nav">
  <span class="active" style="width:106px">Home</span>
  <span style="width:120px">About</span>
  <span style="width:112px">Serives</span>
  <span style="width:116px">Blog</span>
  <span style="width:104px">News</span>
  <span style="width:163px">Contact Us</span>
</nav>

<div class="abs hero" role="img" aria-label="Photo of a smiling businessman in a suit with a blurred team of colleagues behind him"></div>
<div class="abs hero-shadow"></div>
<div class="abs hero-title">KEYSTONE BRIDGE ADVISORY</div>
<div class="abs arrow" style="left:84px;top:264px"><svg width="8" height="10" viewBox="0 0 8 10"><path d="M6 1L2 5l4 4" fill="none" stroke="#333" stroke-width="2"/></svg></div>
<div class="abs arrow" style="left:755px;top:264px"><svg width="8" height="10" viewBox="0 0 8 10"><path d="M2 1l4 4-4 4" fill="none" stroke="#333" stroke-width="2"/></svg></div>
<div class="abs dots"><i class="on"></i><i></i><i></i></div>

<h1 class="abs welcome">Welcome To <b>KBA</b></h1>
<p class="abs intro">Lorem ipsum dolor sit amet, consectetuer adipiscing elit, sed diam nonummy nibh euismod tincidunt ut laoreet dolore magna aliquam erat volutpat. Ut wisi enim ad minim veniam, quis nostrud exerci tation ullamcorper suscipit lobortis nisl ut aliquip ex ea commodo consequat.  Lorem ipsum dolor sit amet, consectetuer adipiscing elit, sed diam nonummy nibh euismod tincidunt ut laoreet dolore magna aliquam erat volutpat. Ut wisi enim ad minim veniam, quis nostrud exerci tation ullamcorper suscipit lobortis nisl ut aliquip ex ea commodo consequat.</p>

<h2 class="abs section-title" style="left:72px;top:586px">Services</h2>
<div class="abs services">
  <div class="card teal"><h3>Interim Management</h3><p>Lorem ipsum dolor sit amet, consec-tetuer adipiscing elit, sed diam nonummy nibh euismod tincidunt ut laoreet dolore magna aliquam erat volutpat.<br>Read more..</p></div>
  <div class="photo-meeting" role="img" aria-label="Photo of business people meeting around a glass table with a laptop"></div>
  <div class="card orange"><h3>Executive Transition</h3><p>Lorem ipsum dolor sit amet, consec-tetuer adipiscing elit, sed diam nonummy nibh euismod tincidunt ut laoreet dolore magna aliquam erat volutpat.<br>Read more..</p></div>
  <div class="photo-digital" role="img" aria-label="Illustration of a head surrounded by floating digital image panels"></div>
</div>

<div class="abs lower"></div>
<div class="abs heading-row" style="left:72px;top:782px;width:352px"><span>Recent News</span><i></i></div>
<div class="abs heading-row" style="left:438px;top:782px;width:352px"><span>Choose Us</span><i></i></div>

<div class="abs date" style="left:74px;top:825px">20<br>FEb</div>
<div class="abs pen" style="left:127px;top:825px"><svg width="20" height="20" viewBox="0 0 20 20"><path d="M3 17l1-4L14 3l3 3L7 16z" fill="#666"/><path d="M3 17l1-4 3 3z" fill="#333"/></svg></div>
<div class="abs post" style="left:188px;top:824px"><h4>Standart Post Type</h4><p>Proin gravida nibh vel velit auctor aliquet. Aenean sollicitudin, lorem quis bibendum auctor, nisi elit consequat ipsum, nec sagittis...</p></div>

<div class="abs date" style="left:74px;top:923px">20<br>FEb</div>
<div class="abs pen" style="left:127px;top:923px"><svg width="20" height="20" viewBox="0 0 20 20"><path d="M3 17l1-4L14 3l3 3L7 16z" fill="#666"/><path d="M3 17l1-4 3 3z" fill="#333"/></svg></div>
<div class="abs post" style="left:188px;top:922px"><h4>Post with Featured Image</h4><p>Proin gravida nibh vel velit auctor aliquet. Aenean sollicitudin, lorem quis bibendum auctor, nisi elit consequat ipsum, nec sagittis...</p></div>

<div class="abs acc open" style="left:439px;top:815px"><span class="sign">&minus;</span><span class="label">Lorem Ipsum</span></div>
<p class="abs acc-body" style="left:451px;top:859px">Localization Support. You just need to translate and save the translation file. Easy as that! Tidewell is also LinguaPress Plugin ready, in case your business needs a multi language site.</p>
<div class="abs acc" style="left:439px;top:916px"><span class="sign">+</span><span class="label">Morbi leo risus, porta ac consectetur ?</span></div>
<div class="abs acc" style="left:439px;top:954px"><span class="sign">+</span><span class="label">Vivamus sagittis lacus vel augue?</span></div>

<section class="abs newsletter">
  <svg width="865" height="88" viewBox="0 0 865 88"><polygon points="480,0 865,0 865,88 400,88" fill="var(--green-light)"/><polygon points="480,0 400,88 440,88" fill="#98cc5c"/></svg>
</section>
<h2 class="abs nl-title" style="top:1030px">SIGN UP TO OUT NEWSLETTER :</h2>
<p class="abs nl-text" style="top:1059px">Duis autem vel eum iriure dolor in hendrerit in vulputate velit esse mole stie consequat, vel illum dolore eu feugiat nulla facilisis at vero eros et accumsan et iusto odio dignissim qui blandit praesent luptatum.</p>
<div class="abs nl-input" style="top:1050px"></div>
<div class="abs nl-btn" style="top:1050px">SUBSCRIBE</div>

<div class="abs footer-rule"></div>
<footer class="abs footer">
  <div class="links">Home &nbsp;|&nbsp; About us &nbsp;|&nbsp; Services &nbsp;|&nbsp; What works &nbsp;|&nbsp; Contact us</div>
  <div class="copy">Content copyright 2013. KBA. All rights reserved.</div>
  <div class="social"><i></i><i></i><i></i></div>
</footer>
</body>
</html>
```